New Business Card Design Project

I would like my card design to look exactly like the logo, design, layout, and print of the current attached file. The only change I would like made would be for the print to say THE KMR GROUP instead of THE MORALES GROUP. Basically, just replace his group name with my group name. I would also like the backgroud to be the same texture and color as the attached file. I love the dark blue lettering and house logo on the card.

I am completely open to the rest of the card design. I just want something clean and simple. Only basic contact info required on the card. Maybe just name: Wade K Holmer and cell # 555.014.2289 and email wade@kmrhomesteam.com

```html
<!DOCTYPE html>
<html lang="en">
<head>
<meta charset="utf-8">
<title>KMR Group Business Card</title>
<link href="https://fonts.googleapis.com/css2?family=Quicksand:wght@500;600&display=swap" rel="stylesheet">
<style>
  :root {
    --backdrop: #c8c8cb;
    --navy: #1b1733;
    --navy-deep: #141126;
    --cream: #fcecdc;
    --cream-soft: #f3e2d2;
    --ink: #3a3450;
  }
  * { margin: 0; padding: 0; box-sizing: border-box; }
  html, body {
    width: 1200px;
    height: 809px;
    overflow: hidden;
    background: var(--backdrop);
    font-family: "Quicksand", sans-serif;
  }
  .spread {
    position: absolute;
    inset: 0;
    display: flex;
    justify-content: center;
    align-items: center;
    gap: 40px;
  }
  .card {
    position: relative;
    width: 300px;
    height: 525px;
    background: var(--navy);
    overflow: hidden;
    box-shadow: 0 10px 30px rgba(0,0,0,0.25);
  }
  .card-front .cream-shape {
    position: absolute;
    inset: 0;
    width: 100%;
    height: 100%;
  }
  .brand {
    position: absolute;
    display: flex;
    align-items: center;
    gap: 12px;
    font-weight: 600;
    line-height: 1.05;
    text-transform: uppercase;
  }
  .brand-mark {
    display: block;
    background: currentColor;
    flex: none;
  }
  .card-front .brand {
    left: 58px;
    top: 195px;
    color: var(--ink);
    font-size: 26px;
  }
  .card-front .brand-mark { width: 40px; height: 40px; }
  .card-back {
    background: linear-gradient(135deg, #241f40 0%, var(--navy) 45%, var(--navy-deep) 100%);
  }
  .card-back .brand {
    left: 30px;
    top: 52px;
    color: var(--cream-soft);
    font-size: 15px;
    gap: 8px;
  }
  .card-back .brand-mark { width: 24px; height: 24px; }
  .holder-name {
    position: absolute;
    left: 0;
    right: 0;
    top: 188px;
    text-align: center;
    color: var(--cream-soft);
    font-size: 17px;
    font-weight: 500;
    letter-spacing: 0.5px;
  }
  .contact {
    position: absolute;
    left: 145px;
    top: 395px;
    display: flex;
    gap: 10px;
  }
  .contact-rule {
    width: 1px;
    height: 70px;
    background: var(--cream-soft);
    opacity: 0.7;
  }
  .contact-list {
    list-style: none;
    display: flex;
    flex-direction: column;
    justify-content: center;
    gap: 14px;
    color: var(--cream-soft);
    font-size: 9px;
    font-weight: 500;
    white-space: nowrap;
  }
  .contact-list li {
    display: flex;
    align-items: center;
    gap: 7px;
  }
  .contact-icon { width: 12px; height: 12px; flex: none; }
</style>
</head>
<body>
  <main class="spread">
    <section class="card card-front" aria-label="Card front">
      <svg class="cream-shape" viewBox="0 0 300 525" preserveAspectRatio="none" aria-hidden="true">
        <path d="M120,0 L300,0 L300,360 Q255,465 175,525 L0,525 L0,330 Q15,125 120,0 Z" fill="var(--cream)"/>
      </svg>
      <div class="brand">
        <span class="brand-mark"></span>
        <span class="brand-name">KMR<br>Group</span>
      </div>
    </section>

    <section class="card card-back" aria-label="Card back">
      <div class="brand">
        <span class="brand-mark"></span>
        <span class="brand-name">KMR<br>Group</span>
      </div>
      <p class="holder-name">Wade K Holmer</p>
      <div class="contact">
        <span class="contact-rule"></span>
        <ul class="contact-list">
          <li>
            <svg class="contact-icon" viewBox="0 0 12 12" aria-hidden="true">
              <rect x="0.5" y="2" width="11" height="8" fill="var(--cream-soft)"/>
              <path d="M0.5,2 L6,6.5 L11.5,2" fill="none" stroke="var(--navy)" stroke-width="1"/>
            </svg>
            <span>wade@kmrhomesteam.com</span>
          </li>
          <li>
            <svg class="contact-icon" viewBox="0 0 12 12" aria-hidden="true">
              <rect x="3" y="0.5" width="6" height="11" rx="1" fill="none" stroke="var(--cream-soft)" stroke-width="1"/>
              <line x1="5" y1="10" x2="7" y2="10" stroke="var(--cream-soft)" stroke-width="0.8"/>
            </svg>
            <span>555 014 2289</span>
          </li>
        </ul>
      </div>
    </section>
  </main>
</body>
</html>
```